construction company offering modern and striking homes and apartments

I need a card design for my new construction company called Tallow Constructions (vic) Pty Ltd.
We build everything from multi home development sites to modern and edgy apartment complexes.
I am open to any colors used as long as it stands out and doesn't look cheap. I want the final design to show my prospective clients I am a professional construction company

Industry/Entity Type

Construction

```html
<!DOCTYPE html>
<html lang="en">
<head>
<meta charset="utf-8">
<title>Tallow Constructions – Business Card</title>
<link rel="stylesheet" href="https://fonts.googleapis.com/css2?family=Jost:wght@300;400&family=Arimo:wght@400;700&display=swap">
<style>
  :root {
    --bg: #efefef;
    --ink: #1f1b1a;
    --orange: #c65a25;
    --paper: #fbfbf9;
    --text: #2a2a2a;
    --muted: #8a8a8a;
    --badge-green: #3ba546;
  }
  * { box-sizing: border-box; margin: 0; padding: 0; }
  html, body { width: 1112px; height: 1200px; overflow: hidden; }
  body {
    background: radial-gradient(ellipse at 50% 35%, #fafafa 0%, var(--bg) 60%, #e2e2e2 100%);
    font-family: "Arimo", Arial, sans-serif;
    position: relative;
  }

  /* Brand lockup */
  .brand {
    position: absolute; top: 160px; left: 0; width: 100%;
    display: flex; justify-content: center; align-items: center; gap: 22px;
  }
  .brand-dot { width: 112px; height: 112px; border-radius: 50%; background: var(--ink); }
  .brand-name {
    font-family: "Jost", sans-serif; font-weight: 300; color: var(--ink);
    font-size: 34px; line-height: 1.12; letter-spacing: 1.5px; text-transform: uppercase;
  }

  /* Cards */
  .card {
    position: absolute; top: 470px; width: 340px; height: 580px;
    box-shadow: 0 18px 40px rgba(0,0,0,.18), 0 3px 8px rgba(0,0,0,.12);
    overflow: hidden;
  }
  .card-front { left: 180px; background: var(--orange); }
  .card-back  { left: 592px; background: var(--paper); }

  .front-mark {
    position: absolute; top: 170px; left: 80px; width: 180px; height: 180px;
    border-radius: 50%; background: var(--ink);
    display: flex; align-items: center; justify-content: center; text-align: center;
    font-family: "Jost", sans-serif; font-weight: 300; color: #f3e6de;
    font-size: 19px; line-height: 1.2; letter-spacing: 1px; text-transform: uppercase;
  }
  .front-url {
    position: absolute; bottom: 46px; left: 0; width: 100%; text-align: center;
    font-family: "Jost", sans-serif; font-weight: 400; color: #fff; font-size: 19px; letter-spacing: .5px;
  }

  .back-band {
    height: 150px; background: var(--orange);
    display: flex; align-items: center; justify-content: center; gap: 12px;
  }
  .band-dot { width: 46px; height: 46px; border-radius: 50%; background: var(--ink); }
  .band-name {
    font-family: "Jost", sans-serif; font-weight: 300; color: var(--ink);
    font-size: 16px; line-height: 1.1; letter-spacing: 1px; text-transform: uppercase;
  }
  .back-body { padding-top: 34px; text-align: center; color: var(--text); }
  .person-name { color: var(--orange); font-size: 22px; }
  .person-role { font-size: 14px; margin-bottom: 30px; }
  .address { font-size: 15px; line-height: 1.35; }
  .phone { color: var(--orange); font-size: 15px; margin-top: 10px; }
  .email { font-size: 15px; margin-top: 14px; }
  .badges { display: flex; justify-content: center; gap: 20px; margin-top: 30px; }
  .badge-round { width: 42px; height: 42px; border-radius: 50%; border: 3px solid #555; background: #ddd; }
  .badge-square { width: 42px; height: 42px; border-radius: 8px; background: var(--badge-green); }
</style>
</head>
<body>
  <header class="brand">
    <div class="brand-dot"></div>
    <div class="brand-name">Tallow<br>Constructions</div>
  </header>

  <section class="card card-front">
    <div class="front-mark">Tallow<br>Constructions</div>
    <p class="front-url">www.tallowconstructions.com</p>
  </section>

  <section class="card card-back">
    <div class="back-band">
      <div class="band-dot"></div>
      <div class="band-name">Tallow<br>Constructions</div>
    </div>
    <div class="back-body">
      <p class="person-name">Sam Carter</p>
      <p class="person-role">President</p>
      <p class="address">27 Ridge Lane<br>Maple Heights vic 3099</p>
      <p class="phone">555.301.4477</p>
      <p class="email">sam@tallowconstructions.com</p>
      <div class="badges">
        <div class="badge-round"></div>
        <div class="badge-square"></div>
      </div>
    </div>
  </section>
</body>
</html>
```